Design clean technology service-based company website

Hello, We are looking to reskin our company website. We are an environmental inspection company and test for Asbestos, Lead and Mold along with other contaminants. People depend on the results to be accurate and fast. We are regulated by the EPA and State regulations. We work a lot with business to business and business to customer. We are wanting to make our new presentation to be modern and easy for customers to interact with us, understand our process and services while providing valuable environmental informational resource and updates. We are a technology based company and will be providing instantaneous results as reports come in for the customers. We are needing good calls to action on the site to direct them to setup a new inspection. Each user will have a backend access to their job information with invoices, reports, status, etc. We have developed software to be able to proved these reports and want to look the part.

My current website is www.trypelmarix.com

Helllo we are wanting to make sure we have good time to select the right website for us and also have the additional time to select other pages of the website. We have received great designs and have consolidated our requests into a document for the next set of iterations.

Target Market(s)

Home Owners, Contractors, Engineers, Real Estate Agents, Building Owners, Insurance Adjusters

Industry/Entity Type

Environmental Consultant

Number of Pages Required

5+ page

Font styles to use
Sans Serif

Colors
0355a3
9bcb3c
7f7f7f
f5f5f5
000000

Requirements
Must have
• Use our existing logo to design around
• The layouts look good in mobile mode for understanding and selecting services and signing up
• Clean Modern Layout
• Have all pages on the website have a similar layout and feel
• Clearly communicate services along with bundle service packages
• Detail the customer journey with graphic design
• Great call to actions to either schedule inspection online, call, text, chat
Nice to have
• Have an interactive graphic for where to test for lead, asbestos and mold.
• I like the barney kolts top order line bar - see attached
• Have clear question and answer page layouts for asbestos, lead and mold
• Show Company reviews
• Have clear Resources pages for all types of contaminants
Should not have
• My current website is www.trypelmarix.com

```html
<!DOCTYPE html>
<html lang="en">
<head>
<meta charset="utf-8">
<title>Pelmarix Environmental Inspections</title>
<link rel="stylesheet" href="https://fonts.googleapis.com/css2?family=Lato:ital,wght@0,400;0,700;0,900;1,400&display=swap">
<style>
:root{
  --blue:#0355a3;
  --green:#8dc63f;
  --green-dark:#7ab32e;
  --grey:#7f7f7f;
  --light:#f5f5f5;
  --ink:#222;
  --footer:#1f1f1f;
  --white:#fff;
  --star:#f5a623;
}
*{box-sizing:border-box;margin:0;padding:0}
html,body{width:1200px;height:3136px;overflow:hidden}
body{font-family:'Lato',sans-serif;color:var(--ink);background:var(--white);position:relative}
.wrap{width:1050px;margin:0 auto;position:relative}
.btn{display:inline-block;background:var(--green);color:var(--white);font-weight:700;font-size:14px;text-transform:uppercase;letter-spacing:.3px;text-align:center;line-height:44px;height:44px;padding:0 22px;border-radius:2px}

/* header */
.site-header{height:152px;background:var(--white);position:relative;box-shadow:0 1px 3px rgba(0,0,0,.06)}
.brand{position:absolute;left:75px;top:26px;display:flex;align-items:center;gap:12px}
.brand-mark{width:30px;height:30px;border-radius:50%;background:var(--green)}
.brand-name{font-size:40px;font-weight:700;color:var(--green);letter-spacing:-.5px;line-height:1}
.brand-sub{position:absolute;left:75px;top:76px;font-size:11px;letter-spacing:2.6px;color:var(--grey);text-transform:uppercase}
.header-phone{position:absolute;left:680px;top:38px;font-size:21px;font-weight:700;color:var(--blue);display:flex;align-items:center;gap:10px}
.header-cta{position:absolute;right:75px;top:32px;width:240px;padding:0}
.main-nav{position:absolute;top:118px;left:0;right:0;display:flex;justify-content:center;gap:0}
.main-nav a{font-size:12.5px;font-weight:700;color:#333;text-transform:uppercase;padding:0 28px;text-decoration:none;line-height:24px}
.main-nav a.active{color:var(--blue)}

/* hero */
.hero{position:relative;height:528px;overflow:hidden}
.hero-photo{position:absolute;inset:0;background:linear-gradient(100deg,#5d6b83 0%,#8c9bb3 35%,#c5cfdc 60%,#3a5a80 78%,#27486d 100%)}
.hero-copy{position:absolute;left:75px;top:158px;color:var(--white);width:660px}
.hero-copy h1{font-size:41px;font-weight:900;letter-spacing:.3px;line-height:1.1}
.hero-copy p{font-size:24px;font-weight:700;line-height:1.3;margin-top:8px}
.hero-copy .btn{margin-top:22px;font-size:13px;height:42px;line-height:42px}
.hero-dots{position:absolute;left:75px;bottom:48px;display:flex;gap:8px}
.hero-dots span{width:10px;height:10px;border-radius:50%;background:var(--white)}
.hero-dots span.on{background:var(--green)}

/* services */
.services{padding:50px 0 50px}
.service-grid{display:flex;gap:30px}
.service-card{width:330px;border-radius:8px;overflow:hidden}
.service-card .ph{height:298px}
.service-card h3{background:var(--green);color:var(--white);text-align:center;font-size:19px;font-weight:700;line-height:60px;text-transform:uppercase}

/* story */
.story{background:var(--light);height:338px;padding-top:48px}
.story .wrap{display:flex;gap:50px}
.story-col{width:500px}
.story h2{font-size:23px;font-weight:900;color:var(--blue);text-transform:uppercase;margin-bottom:18px}
.story p{font-size:13.5px;line-height:1.6;color:#444;margin-bottom:4px}
.story .btn{margin-top:26px;width:178px;padding:0}

/* about */
.about{height:368px;position:relative}
.owner-photo{position:absolute;left:165px;top:46px;width:280px;height:280px;border-radius:50%;background:radial-gradient(circle at 50% 40%,#b7a894 0%,#6f7c5c 55%,#3c5a34 100%)}
.about-copy{position:absolute;left:496px;top:78px;width:540px}
.about-copy h2{font-size:23px;font-weight:900;color:var(--blue);text-transform:uppercase}
.about-copy h3{font-size:19px;font-weight:700;color:var(--green);text-transform:uppercase;margin-top:24px}
.about-copy .role{font-size:13.5px;font-weight:700;color:var(--blue);margin-top:4px}
.about-copy p{font-size:13.5px;line-height:1.65;color:#444;margin-top:6px}

/* videos */
.videos{background:var(--light);height:446px;padding-top:38px}
.videos h2{text-align:center;font-size:23px;font-weight:900;color:var(--blue);text-transform:uppercase;margin-bottom:24px}
.video-grid{display:flex;gap:26px}
.video{width:512px;height:292px;position:relative}
.video-a{background:linear-gradient(160deg,#3a3a3a 0%,#4b4636 55%,#26231c 100%)}
.video-b{background:linear-gradient(160deg,#e8e4df 0%,#b7aea5 50%,#6b5e52 100%)}
.play{position:absolute;left:50%;top:50%;width:58px;height:58px;margin:-29px 0 0 -29px}

/* reviews */
.reviews{height:400px;padding-top:38px;position:relative}
.reviews h2{text-align:center;font-size:23px;font-weight:900;color:var(--blue);text-transform:uppercase;margin-bottom:30px}
.review-grid{display:flex;gap:30px}
.review{width:330px;text-align:center}
.review blockquote{font-style:italic;font-size:13.5px;line-height:1.9;color:#333;padding:0 24px}
.review cite{display:block;font-style:normal;font-weight:700;color:var(--green);font-size:14px;margin-top:10px}
.stars{display:flex;justify-content:center;gap:3px;margin-top:4px}
.arrow{position:absolute;top:175px}
.arrow.prev{left:50px}
.arrow.next{right:50px}
.reviews .more{display:block;width:178px;margin:40px auto 0;padding:0}

/* accreditations */
.accreditations{background:var(--light);height:195px;display:flex;align-items:center;justify-content:center;gap:42px}
.badge{background:#b9b9b9}

/* footer */
.site-footer{background:var(--footer);height:256px;color:#cfcfcf;position:relative}
.footer-brand{position:absolute;left:75px;top:48px}
.footer-brand .brand-name{font-size:34px;display:flex;align-items:center;gap:10px}
.footer-brand .brand-mark{width:24px;height:24px}
.footer-brand .small{font-size:11px;letter-spacing:2.2px;color:var(--grey);text-transform:uppercase;margin-top:6px}
.footer-brand .legal{font-size:11px;line-height:1.7;color:#9a9a9a;margin-top:14px}
.fcol{position:absolute;top:50px}
.fcol h4{font-size:15px;font-weight:700;color:var(--green);text-transform:uppercase;margin-bottom:16px}
.sitemap{left:352px}
.sitemap ul{list-style:none;display:grid;grid-template-columns:132px 100px;row-gap:13px}
.sitemap li{font-size:12.5px;color:#ddd}
.contact{left:620px}
.contact p{font-size:12.5px;line-height:1.75;color:#ddd}
.contact .line{display:flex;align-items:center;gap:12px;margin-top:6px}
.subscribe{left:888px}
.sub-form{display:flex;width:237px;height:46px;margin-top:2px}
.sub-form span{flex:1;background:var(--white);color:#777;font-size:12px;line-height:46px;padding-left:12px}
.sub-form b{width:46px;background:var(--blue);display:flex;align-items:center;justify-content:center}
.social{display:flex;gap:18px;margin-top:20px;padding-left:3px}
.social span{width:18px;height:18px;border-radius:50%;background:#e6e6e6}
</style>
</head>
<body>

<header class="site-header">
  <div class="brand"><span class="brand-name">Pelmarix</span><span class="brand-mark"></span></div>
  <div class="brand-sub">Environmental Inspections</div>
  <div class="header-phone">
    <svg width="20" height="20" viewBox="0 0 24 24"><path fill="#0355a3" d="M6.6 10.8a15.1 15.1 0 0 0 6.6 6.6l2.2-2.2c.3-.3.7-.4 1-.2 1.1.4 2.3.6 3.6.6.6 0 1 .4 1 1V20c0 .6-.4 1-1 1A17 17 0 0 1 3 4c0-.6.4-1 1-1h3.5c.6 0 1 .4 1 1 0 1.3.2 2.5.6 3.6.1.3 0 .7-.2 1z"/></svg>
    555-214-7730
  </div>
  <a class="btn header-cta">Setup a New Inspection</a>
  <nav class="main-nav">
    <a class="active">Home</a><a>Our Services</a><a>Resources</a><a>Blog</a><a>Q &amp; A</a><a>Reviews</a><a>Connect</a>
  </nav>
</header>

<section class="hero">
  <div class="hero-photo" role="img" aria-label="Smiling inspector in a work uniform holding a clipboard, magnifying glass over a roof in the background"></div>
  <div class="hero-copy">
    <h1>WELCOME TO PELMARIX</h1>
    <p>We are an environmental inspection company and test for Asbestos, Lead and Mold along with other contaminants.</p>
    <a class="btn">Setup a New Inspection</a>
  </div>
  <div class="hero-dots"><span class="on"></span><span></span><span></span><span></span></div>
</section>

<section class="services">
  <div class="wrap service-grid">
    <div class="service-card">
      <div class="ph" role="img" aria-label="Weathered corrugated asbestos roofing sheets" style="background:linear-gradient(160deg,#8d9296,#5a5f63 60%,#3b3f42)"></div>
      <h3>Asbestos Inspection</h3>
    </div>
    <div class="service-card">
      <div class="ph" role="img" aria-label="Inspector in hard hat writing on a clipboard outside a brick house" style="background:linear-gradient(160deg,#c9b59a,#9c7a5c 55%,#6d4c37)"></div>
      <h3>Lead Inspection</h3>
    </div>
    <div class="service-card">
      <div class="ph" role="img" aria-label="Close-up of mold spores growing on a surface" style="background:radial-gradient(circle at 55% 50%,#8c8f84 0%,#5b3b31 55%,#3a221c 100%)"></div>
      <h3>Mold Inspection</h3>
    </div>
  </div>
</section>

<section class="story">
  <div class="wrap">
    <div class="story-col">
      <h2>Environmental Testing Evolved</h2>
      <p>Pelmarix grew up in the rough and tumble disaster restoration industry. Time and time again, we saw projects small and large brought to a stand-still to await environmental testing and results.</p>
      <p>First, we had to know when it's prudent or even required by law to test for asbestos, lead-based paint, mold or other contaminants.</p>
      <a class="btn">Read More</a>
    </div>
    <div class="story-col">
      <h2>The Next Step</h2>
      <p>At Pelmarix, we are experienced in assessing the environmental hazards that merit or even require testing by law. We are trained and certified to safely obtain environmental test samples. And we have established a working relationship with top-rated testing facilities that enable us to get most test results within hours, not days.</p>
      <a class="btn">Read More</a>
    </div>
  </div>
</section>

<section class="about">
  <div class="owner-photo" role="img" aria-label="Portrait of the company owner in a grey suit outdoors"></div>
  <div class="about-copy">
    <h2>About Owner</h2>
    <h3>Dana Whitfield</h3>
    <div class="role">Owner</div>
    <p>In his experience with inspecting property and mitigating environmental issues, Dana saw one project after another brought to a standstill awaiting testing results. He believed property owners should be able to get test results in hours, not days. Pelmarix was born.</p>
  </div>
</section>

<section class="videos">
  <h2>Watch Videos</h2>
  <div class="wrap video-grid">
    <div class="video video-a" role="img" aria-label="Video still: workers removing asbestos material">
      <svg class="play" viewBox="0 0 58 58"><circle cx="29" cy="29" r="29" fill="#fff"/><path d="M23 18l18 11-18 11z" fill="#333"/></svg>
    </div>
    <div class="video video-b" role="img" aria-label="Video still: interior window frame with mold damage">
      <svg class="play" viewBox="0 0 58 58"><circle cx="29" cy="29" r="29" fill="#fff"/><path d="M23 18l18 11-18 11z" fill="#333"/></svg>
    </div>
  </div>
</section>

<section class="reviews">
  <h2>Reviews</h2>
  <svg class="arrow prev" width="20" height="40" viewBox="0 0 20 40"><path d="M17 2L3 20l14 18" fill="none" stroke="#bbb" stroke-width="2"/></svg>
  <svg class="arrow next" width="20" height="40" viewBox="0 0 20 40"><path d="M3 2l14 18L3 38" fill="none" stroke="#bbb" stroke-width="2"/></svg>
  <div class="wrap review-grid">
    <div class="review">
      <blockquote>" I am in the process of remodeliong my kitchen when I was told since the house was built in 1972 if has to have abestos and lead paint test done, went on the..."</blockquote>
      <cite>J.T.</cite>
      <div class="stars"><svg width="80" height="14" viewBox="0 0 80 14"><g fill="#f5a623"><path id="s" d="M7 0l2 4.6 5 .5-3.8 3.3 1.1 4.9L7 10.8 2.7 13.3l1.1-4.9L0 5.1l5-.5z"/><use href="#s" x="16"/><use href="#s" x="32"/><use href="#s" x="48"/><use href="#s" x="64"/></g></svg></div>
    </div>
    <div class="review">
      <blockquote>" I am in the process of remodeliong my kitchen when I was told since the house was built in 1972 if has to have abestos and lead paint test done, went on the..."</blockquote>
      <cite>J.T.</cite>
      <div class="stars"><svg width="80" height="14" viewBox="0 0 80 14"><g fill="#f5a623"><use href="#s"/><use href="#s" x="16"/><use href="#s" x="32"/><use href="#s" x="48"/><use href="#s" x="64"/></g></svg></div>
    </div>
    <div class="review">
      <blockquote>" I am in the process of remodeliong my kitchen when I was told since the house was built in 1972 if has to have abestos and lead paint test done, went on the..."</blockquote>
      <cite>J.T.</cite>
      <div class="stars"><svg width="80" height="14" viewBox="0 0 80 14"><g fill="#f5a623"><use href="#s"/><use href="#s" x="16"/><use href="#s" x="32"/><use href="#s" x="48"/><use href="#s" x="64"/></g></svg></div>
    </div>
  </div>
  <a class="btn more">Read All Reviews</a>
</section>

<section class="accreditations">
  <div class="badge" style="width:275px;height:60px;border-radius:4px"></div>
  <div class="badge" style="width:128px;height:128px;border-radius:50%"></div>
  <div class="badge" style="width:160px;height:60px;border-radius:4px"></div>
  <div class="badge" style="width:180px;height:70px;border-radius:4px"></div>
  <div class="badge" style="width:175px;height:60px;border-radius:4px"></div>
</section>

<footer class="site-footer">
  <div class="footer-brand">
    <div class="brand-name">Pelmarix<span class="brand-mark"></span></div>
    <div class="small">Environmental Inspections</div>
    <div class="legal">Copyright © 2018<br>Pelmarix Environmental Inspections<br>All Right Reserved</div>
  </div>
  <div class="fcol sitemap">
    <h4>Site Map</h4>
    <ul><li>Home</li><li>Q &amp; A</li><li>Our Services</li><li>Reviews</li><li>Resources</li><li>Connect</li><li>Blog</li></ul>
  </div>
  <div class="fcol contact">
    <h4>Contact Address</h4>
    <p>420 Meridian Ave. Ste.<br>210 Lakewood,<br>Co. 80000</p>
    <div class="line">
      <svg width="14" height="14" viewBox="0 0 24 24"><path fill="#ddd" d="M6.6 10.8a15.1 15.1 0 0 0 6.6 6.6l2.2-2.2c.3-.3.7-.4 1-.2 1.1.4 2.3.6 3.6.6.6 0 1 .4 1 1V20c0 .6-.4 1-1 1A17 17 0 0 1 3 4c0-.6.4-1 1-1h3.5c.6 0 1 .4 1 1 0 1.3.2 2.5.6 3.6.1.3 0 .7-.2 1z"/></svg>
      <p>555-214-7730</p>
    </div>
    <div class="line">
      <svg width="14" height="12" viewBox="0 0 14 12"><rect width="14" height="12" rx="1" fill="#ddd"/><path d="M0 1l7 5 7-5" fill="none" stroke="#1f1f1f" stroke-width="1.4"/></svg>
      <p>info at trypelmarix.com</p>
    </div>
  </div>
  <div class="fcol subscribe">
    <h4>Email Subscribe</h4>
    <div class="sub-form"><span>Enter Email</span><b><svg width="12" height="16" viewBox="0 0 12 16"><path d="M2 2l7 6-7 6" fill="none" stroke="#fff" stroke-width="2.4"/></svg></b></div>
    <div class="social"><span></span><span></span><span></span><span></span><span></span><span></span></div>
  </div>
</footer>

</body>
</html>
```